We need a business card design for a Dubai based company .

We need a business card for a Dubai based company called "Zernova". We mainly import Flavoured Tobacco products and Charcoal which is used for smoking in a Hookah/Shisha and distribute to the wholesalers and retailers. Logo file is attached herewith.

```html
<!DOCTYPE html>
<html lang="en">
<head>
<meta charset="utf-8">
<title>Zernova Business Card</title>
<link rel="stylesheet" href="https://fonts.googleapis.com/css2?family=Lato:wght@400;700&family=Oswald:wght@500&display=swap">
<style>
  :root {
    --backdrop: #262626;
    --card: #111111;
    --accent: #c0393e;
    --ink: #ffffff;
    --rule: #8a8a8a;
  }
  * { margin: 0; padding: 0; box-sizing: border-box; }
  html, body {
    width: 1200px; height: 900px; overflow: hidden;
    background: var(--backdrop);
    font-family: "Lato", sans-serif;
    color: var(--ink);
  }
  .canvas {
    width: 1200px; height: 900px;
    display: flex; flex-direction: column; align-items: center; justify-content: center;
    gap: 40px;
  }
  .card {
    position: relative;
    width: 660px; height: 377px;
    background: var(--card);
    box-shadow: 0 10px 28px rgba(0,0,0,.55);
    overflow: hidden;
  }
  .card::after {
    content: ""; position: absolute; left: 0; right: 0; bottom: 0;
    height: 11px; background: var(--accent);
  }
  /* front */
  .brand {
    position: absolute; left: 0; right: 0; top: 0; bottom: 40px;
    display: flex; align-items: center; justify-content: center; gap: 18px;
  }
  .brand-square { width: 22px; height: 22px; background: var(--accent); }
  .brand-name {
    font-weight: 400; color: var(--ink); line-height: 1;
    font-size: 54px; letter-spacing: 12px;
  }
  /* back */
  .person { position: absolute; left: 120px; top: 148px; text-align: right; width: 186px; }
  .person-name {
    font-family: "Oswald", sans-serif; font-weight: 500;
    font-size: 30px; color: var(--accent); text-transform: uppercase; line-height: 1;
    letter-spacing: -0.5px;
  }
  .person-title { font-size: 16px; margin-top: 6px; }
  .divider {
    position: absolute; left: 328px; top: 140px; width: 1px; height: 90px; background: var(--rule);
  }
  .contacts { position: absolute; left: 350px; top: 148px; list-style: none; }
  .contacts li { display: flex; align-items: center; gap: 10px; font-size: 16px; height: 26px; }
  .contacts svg { width: 16px; height: 16px; flex: none; }
  .address { position: absolute; left: 130px; bottom: 42px; font-size: 16px; }
</style>
</head>
<body>
<main class="canvas">
  <section class="card card-front">
    <div class="brand">
      <span class="brand-square"></span>
      <div class="brand-name">ZERNOVA</div>
    </div>
  </section>

  <section class="card card-back">
    <div class="person">
      <div class="person-name">Marcus Hale</div>
      <div class="person-title">Managing Director</div>
    </div>
    <div class="divider"></div>
    <ul class="contacts">
      <li>
        <svg viewBox="0 0 24 24" aria-hidden="true"><path fill="#c0393e" d="M6.6 10.8a15 15 0 0 0 6.6 6.6l2.2-2.2c.3-.3.7-.4 1-.2 1.1.4 2.3.6 3.6.6.6 0 1 .4 1 1V20c0 .6-.4 1-1 1A17 17 0 0 1 3 4c0-.6.4-1 1-1h3.5c.6 0 1 .4 1 1 0 1.3.2 2.5.6 3.6.1.3 0 .7-.2 1z"/></svg>
        044-555 018 273
      </li>
      <li>
        <svg viewBox="0 0 24 24" aria-hidden="true"><rect x="2" y="5" width="20" height="14" fill="#c0393e"/><path d="M2 5l10 8 10-8" fill="none" stroke="#111" stroke-width="1.6"/></svg>
        info@zernovatrading.com
      </li>
      <li>
        <svg viewBox="0 0 24 24" aria-hidden="true"><g fill="none" stroke="#c0393e" stroke-width="1.8"><circle cx="12" cy="12" r="9.5"/><ellipse cx="12" cy="12" rx="4" ry="9.5"/><path d="M2.5 12h19M4 7h16M4 17h16"/></g></svg>
        www.zernovatrading.com
      </li>
    </ul>
    <p class="address">17, Al Quoz Street, Dubai, UAE, 00000</p>
  </section>
</main>
</body>
</html>
```